Retail Package for Ammunition Company

We are looking for a packaging design for a retail boxed ammunition. The "look". Attached will be the logo to be used. The logo is attached and a can be manipulated on the box. Box to represent strength and accuracy. Will need to provide .psd files to allow in house personnel to add/remove text to other calibers and warnings. Wow me with your designs!

Browse Other Brands: http://www.brightfalconstore.com/brands

The packaging needs to include:
Logo- provided and the following text:

FRONT 1. 9mm 115gr FMJ

BACK 2. WARNING: To avoid serious injury: (1) use only ammunition in good condition; use only in modern firearms in good condition marked for .22 Long Rifle (LR) cartridges; (2) always be sure barrel is free of any obstructions; the barrel should be checked in case of light recoil, or an unusually loud or weak sound heard during firing; (3) wear eye and ear protection; (4) if gun fails to fire, avoid exposure to breech when unloading and point muzzle in a safe direction. Keep firearm pointed in safe direction at all times; (5) discharge may occur if rim is struck; handle with caution, do not drop. (6) Do not shoot at hard surfaces or water to prevent ricochet; (7) Bullet is capable of traveling extreme distances. Know your backstop; (8) Store in cool dry place

3. LEAD WARNING: Discharging firearms in poorly ventilated areas, cleaning firearms, or handling ammunition may result in exposure to lead and other substances known to cause birth defects, reproductive harm, and other serious physical injury. Have adequate ventilation at all times. Wash hands thoroughly after exposure.

Dimensions ; (LxWxH): 5.25" x 2.625" x 1.125"

Target Market(s)

Ammunition Industry

```html
<!DOCTYPE html>
<html lang="en">
<head>
<meta charset="utf-8">
<title>Crimson Talon Armory – 9mm 115gr FMJ Retail Box</title>
<link rel="stylesheet" href="https://fonts.googleapis.com/css2?family=Montserrat:wght@600;700;800;900&display=swap">
<style>
  :root {
    --canvas: #f3f3f3;
    --box-white: #ffffff;
    --brand-red: #8e1b1f;
    --maroon: #7a1a1c;
    --maroon-deep: #4f0c0e;
    --side-maroon: #5a2424;
    --gold: #e9c56b;
    --dot-grey: #ececec;
  }
  * { box-sizing: border-box; margin: 0; padding: 0; }
  html, body {
    width: 1200px; height: 750px; overflow: hidden;
    background: var(--canvas);
    font-family: "Montserrat", sans-serif;
  }
  .panel { position: absolute; overflow: hidden; }

  /* ---------- top panel ---------- */
  .panel-top {
    left: 270px; top: 75px; width: 840px; height: 180px;
    background: var(--box-white);
  }
  .top-band {
    position: absolute; left: 0; right: 0; bottom: 0; height: 95px;
    background: linear-gradient(90deg, #ffffff 0%, var(--maroon) 45%, var(--maroon-deep) 100%);
  }
  .top-brand {
    position: absolute; left: 0; right: 0; top: 22px; text-align: center;
    color: var(--brand-red); font-weight: 800;
  }
  .top-brand-name { font-size: 28px; line-height: 1; letter-spacing: 1px; }
  .top-brand-sub { font-size: 11px; letter-spacing: 6px; margin-top: 6px; }
  .top-spec {
    position: absolute; left: 0; right: 0; bottom: 26px; text-align: center;
    color: var(--gold); font-weight: 800;
  }
  .top-spec-name { font-size: 18px; line-height: 1.1; }
  .top-spec-sub { font-size: 12px; font-weight: 700; margin-top: 3px; }

  /* ---------- side panel ---------- */
  .panel-side {
    left: 90px; top: 255px; width: 180px; height: 420px;
    background: linear-gradient(180deg, #4e1e20 0%, var(--side-maroon) 55%, #6a2626 100%);
  }
  .side-spec {
    position: absolute; left: 0; right: 0; bottom: 60px; text-align: center;
    color: var(--gold); font-weight: 800;
  }
  .side-caliber { font-size: 24px; line-height: 1; }
  .side-type { font-size: 11px; font-weight: 700; margin-top: 8px; }
  .side-type-sub { font-size: 10px; font-weight: 700; margin-top: 3px; }

  /* ---------- front panel ---------- */
  .panel-front {
    left: 270px; top: 255px; width: 840px; height: 420px;
    background: var(--box-white);
  }
  .band-art { position: absolute; inset: 0; width: 840px; height: 420px; }
  .dot-burst {
    position: absolute; left: 50px; top: 40px; width: 190px; height: 190px;
    border-radius: 50%;
    background: radial-gradient(circle, rgba(236,236,236,0) 40%, var(--dot-grey) 62%, rgba(236,236,236,0) 76%);
  }
  .category-label {
    position: absolute; left: 70px; top: 98px;
    color: var(--brand-red); font-weight: 800; font-size: 27px; line-height: 1.02;
  }
  .header-divider {
    position: absolute; left: 300px; top: 45px; width: 2px; height: 105px;
    background: var(--brand-red);
  }
  .brand-lockup {
    position: absolute; left: 335px; top: 50px; width: 470px; text-align: center;
    color: var(--brand-red); font-weight: 800;
  }
  .brand-name { font-size: 44px; line-height: 1; letter-spacing: 1px; white-space: nowrap; }
  .brand-sub {
    display: flex; align-items: center; gap: 14px; margin-top: 12px;
    font-size: 18px; letter-spacing: 7px;
  }
  .brand-sub::before, .brand-sub::after {
    content: ""; flex: 1; height: 3px; background: var(--brand-red);
  }
  .count-label {
    position: absolute; right: 48px; top: 186px;
    color: #fff; font-weight: 700; font-size: 13px; letter-spacing: 5px;
  }
  .headline {
    position: absolute; right: 45px; top: 220px; text-align: right;
    color: var(--brand-red); font-weight: 900; font-size: 31px; line-height: 0.98;
  }
  .cartridge-art {
    position: absolute; left: 165px; top: 262px; width: 60px; height: 145px;
    background: linear-gradient(90deg, #b8913f, #e9cf84 50%, #c29b48);
  }
  .caliber {
    position: absolute; left: 268px; top: 336px; color: var(--gold); font-weight: 800;
  }
  .caliber-size { font-size: 46px; line-height: 0.95; }
  .caliber-weight { font-size: 27px; line-height: 1; }
  .spec-divider {
    position: absolute; left: 458px; top: 334px; width: 2px; height: 74px;
    background: var(--gold);
  }
  .bullet-type {
    position: absolute; left: 488px; top: 346px; color: var(--gold); font-weight: 800;
  }
  .bullet-type-name { font-size: 24px; line-height: 1; white-space: nowrap; }
  .bullet-type-sub { font-size: 14px; font-weight: 700; margin-top: 6px; }
</style>
</head>
<body>
  <section class="panel panel-top">
    <div class="top-band"></div>
    <div class="top-brand">
      <p class="top-brand-name">CRIMSON TALON</p>
      <p class="top-brand-sub">ARMORY</p>
    </div>
    <div class="top-spec">
      <p class="top-spec-name">FULL METAL JACKET</p>
      <p class="top-spec-sub">FMJ | ELITE AMMUNITION</p>
    </div>
  </section>

  <section class="panel panel-side">
    <div class="side-spec">
      <p class="side-caliber">9mm 115gr</p>
      <p class="side-type">FULL METAL JACKET</p>
      <p class="side-type-sub">FMJ / ELITE AMMUNITION</p>
    </div>
  </section>

  <main class="panel panel-front">
    <svg class="band-art" viewBox="0 0 840 420" aria-hidden="true">
      <defs>
        <linearGradient id="countBandFill" x1="0" x2="1" y1="0" y2="0">
          <stop offset="0" stop-color="#ffffff"/>
          <stop offset="0.55" stop-color="#6b6b6b"/>
          <stop offset="1" stop-color="#1b1b1b"/>
        </linearGradient>
        <linearGradient id="specBandFill" x1="0" x2="1" y1="0" y2="0">
          <stop offset="0" stop-color="#ffffff"/>
          <stop offset="0.3" stop-color="#7a1a1c"/>
          <stop offset="1" stop-color="#6a1416"/>
        </linearGradient>
      </defs>
      <polygon points="225,180 818,180 808,209 225,209" fill="url(#countBandFill)"/>
      <polygon points="0,318 812,318 782,420 0,420" fill="url(#specBandFill)"/>
    </svg>

    <div class="dot-burst" role="img" aria-label="Faint grey dotted burst pattern"></div>
    <p class="category-label">CENTERFIRE<br>CARTRIDGES</p>
    <span class="header-divider"></span>

    <div class="brand-lockup">
      <p class="brand-name">CRIMSON TALON</p>
      <p class="brand-sub">ARMORY</p>
    </div>

    <p class="count-label">50 CARTRIDGES PER BOX</p>

    <h1 class="headline">ELITE<br>PERFORMANCE<br>AMMUNITION</h1>

    <div class="cartridge-art" role="img" aria-label="Photo of a brass 9mm full metal jacket cartridge"></div>

    <div class="caliber">
      <p class="caliber-size">9mm</p>
      <p class="caliber-weight">115gr</p>
    </div>
    <span class="spec-divider"></span>
    <div class="bullet-type">
      <p class="bullet-type-name">FULL METAL JACKET</p>
      <p class="bullet-type-sub">FMJ / ELITE AMMUNITION</p>
    </div>
  </main>
</body>
</html>
```